Dr. Pell Works
Business card, stationary, fax page, envelope
Dr. Pell Works - Corporate Services
Creative Brief
Bright & Fun-filled
Grant Bevis Hallworth
Senior Account Executive
417 S. Tavish Ave Los Angeles CA 90012
grant@drpellworks.example
drpellworks.example
I also have 4 other people that need their won business cards but with their cell phone and title info.

```html
<!DOCTYPE html>
<html lang="en">
<head>
<meta charset="utf-8">
<title>Dr. Pell Works – Stationery</title>
<link href="https://fonts.googleapis.com/css2?family=Archivo+Black&family=Arimo:wght@400;700&display=swap" rel="stylesheet">
<style>
:root{
  --stage:#6a6a6a;
  --ink:#111111;
  --sun:#f7d417;
  --paper:#ffffff;
  --muted:#8a8a8a;
  --rule:#9a9a9a;
  --skin:#f0c9a6;
}
*{box-sizing:border-box;margin:0;padding:0}
html,body{width:1200px;height:562px;overflow:hidden;background:var(--stage)}
body{position:relative;font-family:"Arimo",Arial,sans-serif;color:var(--ink)}
.sheet{position:absolute;background:var(--paper);overflow:hidden}
.brand{display:flex;align-items:center;justify-content:center;gap:6px;color:var(--paper);
  font-family:"Archivo Black","Arial Black",sans-serif;white-space:nowrap}
.brand-dot{border-radius:50%;background:var(--skin);flex:none}
.band-top{position:absolute;left:0;top:0;width:100%;height:52px;background:var(--ink)}
.band-top .brand{height:100%;font-size:15px}
.band-top .brand-dot{width:30px;height:30px}
.band-foot{position:absolute;left:0;bottom:0;width:100%;height:28px;background:var(--sun)}
.foot-text{position:absolute;left:0;bottom:32px;width:100%;text-align:center;font-size:5px;line-height:7px;color:var(--muted)}

/* letterhead */
.letterhead{left:79px;top:72px;width:310px;height:408px}

/* fax */
.fax{left:437px;top:72px;width:312px;height:408px}
.fax-mark{position:absolute;left:106px;top:180px;width:100px;height:100px;border-radius:50%;background:var(--sun);opacity:.12}
.fax-title{position:absolute;left:24px;top:148px;font-family:"Arimo",sans-serif;font-weight:400;font-size:22px;letter-spacing:1px}
.fax-row{position:absolute;left:24px;width:264px;height:14px;border-bottom:1px solid var(--rule);font-size:5.5px;color:#555}
.fax-row span{position:absolute;bottom:2px}
.fax-row span:last-child{left:130px}
.fax-checks{position:absolute;left:24px;top:330px;width:270px;display:flex;justify-content:space-between;font-size:5.5px;color:#555}
.fax-checks span{display:flex;align-items:center;gap:3px}
.fax-checks i{width:6px;height:6px;border:1px solid #666;display:inline-block}

/* business cards */
.card-front{left:826px;top:74px;width:122px;height:70px;background:var(--ink)}
.card-front .brand{position:absolute;left:0;top:6px;width:100%;font-size:10px;gap:4px}
.card-front .brand-dot{width:18px;height:18px}
.card-person{position:absolute;left:0;top:34px;width:100%;text-align:center;color:var(--paper);font-size:5px;line-height:7px}
.card-person b{font-size:6px}
.card-front .card-strip{position:absolute;left:0;bottom:0;width:100%;height:12px;background:var(--sun)}
.card-strip p{font-size:4px;line-height:12px;text-align:center}
.card-back{left:960px;top:74px;width:125px;height:70px;background:var(--sun)}
.card-back .art{position:absolute;right:0;top:0;width:62px;height:70px;background:radial-gradient(circle at 50% 50%,#f7e2cf,#f0c9a6 60%,var(--paper))}

/* envelope */
.envelope{left:826px;top:182px;width:259px;height:171px}
.env-brand{position:absolute;left:0;top:0;width:259px;height:44px;background:var(--ink)}
.env-brand .brand{position:absolute;left:8px;top:0;height:100%;font-size:11px;gap:5px}
.env-brand .brand-dot{width:24px;height:24px}
.env-mark{position:absolute;left:150px;top:62px;width:70px;height:70px;border-radius:50%;background:var(--sun);opacity:.12}
.env-return{position:absolute;left:0;bottom:0;width:86px;height:58px;background:var(--sun);padding:10px 6px;font-size:4.5px;line-height:6.5px}
.env-web{position:absolute;left:92px;bottom:8px;font-size:4.5px;color:var(--muted)}

/* envelope back */
.envelope-back{left:826px;top:372px;width:259px;height:132px}
.envelope-back svg{position:absolute;left:0;top:0}
</style>
</head>
<body>

<section class="sheet letterhead" aria-label="Letterhead">
  <header class="band-top"><div class="brand"><span class="brand-dot"></span>Dr. Pell Works</div></header>
  <p class="foot-text">417 S. Tavish Ave Los Angeles CA 90012<br>grant@drpellworks.example · drpellworks.example</p>
  <footer class="band-foot"></footer>
</section>

<section class="sheet fax" aria-label="Fax cover page">
  <header class="band-top"><div class="brand"><span class="brand-dot"></span>Dr. Pell Works</div></header>
  <div class="fax-mark"></div>
  <h1 class="fax-title">FAX</h1>
  <div class="fax-row" style="top:178px"><span>To:</span><span>From:</span></div>
  <div class="fax-row" style="top:194px"><span>Fax:</span><span>Pages:</span></div>
  <div class="fax-row" style="top:210px"><span>Phone:</span><span>Date:</span></div>
  <div class="fax-row" style="top:226px"><span>Re:</span><span>CC:</span></div>
  <div class="fax-checks">
    <span><i></i>Urgent</span><span><i></i>For Review</span><span><i></i>Please Comment</span><span><i></i>Please Reply</span><span><i></i>Please Recycle</span>
  </div>
  <p class="foot-text">417 S. Tavish Ave Los Angeles CA 90012<br>grant@drpellworks.example · drpellworks.example</p>
  <footer class="band-foot"></footer>
</section>

<section class="sheet card-front" aria-label="Business card front">
  <div class="brand"><span class="brand-dot"></span>Dr. Pell Works</div>
  <p class="card-person"><b>Grant Bevis Hallworth</b><br>Senior Account Executive</p>
  <div class="card-strip"><p>grant@drpellworks.example · drpellworks.example</p></div>
</section>

<section class="sheet card-back" aria-label="Business card back">
  <div class="art" role="img" aria-label="Brand character illustration"></div>
</section>

<section class="sheet envelope" aria-label="Envelope front">
  <div class="env-brand"><div class="brand"><span class="brand-dot"></span>Dr. Pell Works</div></div>
  <div class="env-mark"></div>
  <address class="env-return" style="font-style:normal">Dr. Pell Works<br>417 S. Tavish Ave<br>Los Angeles CA 90012</address>
  <p class="env-web">drpellworks.example</p>
</section>

<section class="sheet envelope-back" aria-label="Envelope back">
  <svg width="259" height="132" viewBox="0 0 259 132">
    <path d="M0 0 H259 V10 Q190 40 129.5 62 Q69 40 0 10 Z" fill="var(--sun)"/>
    <path d="M0 10 Q69 40 129.5 62 Q190 40 259 10" fill="none" stroke="#d9b800" stroke-width="1"/>
  </svg>
</section>

</body>
</html>
```